Illustrated restaurant promotional posters

We need series of 5 promotional posters for a restaurant, each one promoting a different special across the week. The text for each poster must be included and is in the file attached to this brief, but the design should only be treated as a draft idea for what we are looking for (we are flexible). We're looking to add illustrations to these posters, which may or may not require a complete re-imagining. The restaurant serves American BBQ with a latin twist, is smart casual, and the poster should reflect a welcoming, casual, but also elegant establishment. Images of food and the venue can be found here https://www.cedarforkgrillhouse.com/

Target Market(s)

18 to 65, broad range of people, local restaurant, people popping in for a quick bite, and also celebrating main events

Industry/Entity Type

Restaurant

Font styles to use
Sans Serif

Colors
0054AA
0677BA
7BADD7
CADEEF
E8F1F8
EB3D1F
EC4F4E
F09395
F8D3D4
FCEDEE

Requirements
Must have
• Each poster must contain the text that is in the attached draft poster, illustration
Nice to have
• Colours similar to what is in attached file, though open to other otions

```html
<!DOCTYPE html>
<html lang="en">
<head>
<meta charset="utf-8">
<title>Tuesday Special – Cedar Fork Grillhouse</title>
<link rel="stylesheet" href="https://fonts.googleapis.com/css2?family=Allura&family=Bebas+Neue&family=Oswald:wght@700&family=Montserrat:wght@500;700&display=swap">
<style>
  :root {
    --navy: #1f2233;
    --white: #ffffff;
    --red: #ec4f4e;
    --dot-grey: rgba(190, 194, 204, 0.55);
    --soft-white: rgba(255, 255, 255, 0.10);
  }
  html, body {
    margin: 0;
    padding: 0;
    overflow: hidden;
    background: var(--navy);
  }
  .poster {
    position: relative;
    width: 848px;
    height: 1200px;
    background: var(--navy);
    overflow: hidden;
    font-family: "Montserrat", sans-serif;
    color: var(--white);
  }
  .dot-texture {
    position: absolute;
    width: 210px;
    height: 185px;
  }
  .dot-texture--left {
    left: 0; top: 0;
    background: radial-gradient(ellipse at 0% 0%, var(--dot-grey) 0%, rgba(190,194,204,0.15) 55%, transparent 75%);
  }
  .dot-texture--right {
    right: 0; top: 0;
    background: radial-gradient(ellipse at 100% 0%, var(--dot-grey) 0%, rgba(190,194,204,0.15) 55%, transparent 75%);
  }
  .day-script {
    position: absolute;
    left: 300px;
    top: 86px;
    width: 240px;
    text-align: center;
    font-family: "Allura", cursive;
    font-size: 118px;
    line-height: 1;
    margin: 0;
  }
  .special-title {
    position: absolute;
    left: 223px;
    top: 244px;
    width: 410px;
    margin: 0;
    font-family: "Bebas Neue", sans-serif;
    font-weight: 400;
    font-size: 192px;
    line-height: 1;
    letter-spacing: -1px;
    transform: scaleX(0.8);
    transform-origin: left top;
    white-space: nowrap;
  }
  .pointer-arrow {
    position: absolute;
    left: 0; top: 0;
    width: 848px;
    height: 1200px;
    pointer-events: none;
  }
  .price-badge {
    position: absolute;
    left: 674px;
    top: 394px;
    width: 114px;
    height: 114px;
    border-radius: 50%;
    background: var(--white);
    display: flex;
    align-items: center;
    justify-content: center;
    font-family: "Oswald", sans-serif;
    font-weight: 700;
    font-size: 44px;
    color: var(--red);
    letter-spacing: -1px;
  }
  .price-unit {
    position: absolute;
    left: 643px;
    top: 510px;
    font-size: 30px;
    font-weight: 500;
    letter-spacing: 2px;
  }
  .dish-illustration {
    position: absolute;
    left: 223px;
    top: 449px;
    width: 401px;
    height: 336px;
    border-radius: 24px;
    background: var(--soft-white);
  }
  .actions {
    position: absolute;
    left: 59px;
    top: 871px;
    display: flex;
    gap: 38px;
  }
  .action-button {
    width: 220px;
    height: 54px;
    border-radius: 27px;
    background: var(--red);
    color: var(--white);
    display: flex;
    align-items: center;
    justify-content: center;
    font-size: 21px;
    font-weight: 500;
    letter-spacing: 0.5px;
    text-decoration: none;
  }
  .brand-name {
    position: absolute;
    left: 324px;
    top: 1018px;
    width: 200px;
    text-align: center;
    font-weight: 700;
    font-size: 22px;
    line-height: 1.3;
    letter-spacing: 3px;
  }
</style>
</head>
<body>
<main class="poster">
  <div class="dot-texture dot-texture--left" role="img" aria-label="Halftone dot pattern in the corner"></div>
  <div class="dot-texture dot-texture--right" role="img" aria-label="Halftone dot pattern in the corner"></div>

  <p class="day-script">Tuesday</p>
  <h1 class="special-title">SPECIAL</h1>

  <svg class="pointer-arrow" viewBox="0 0 848 1200" aria-hidden="true">
    <path d="M636 318 C 650 290, 680 280, 700 290 C 725 302, 738 335, 737 368" fill="none" stroke="#ffffff" stroke-width="5" stroke-linecap="round"/>
    <path d="M718 350 L737 370 L760 349" fill="none" stroke="#ffffff" stroke-width="5" stroke-linecap="round" stroke-linejoin="round"/>
  </svg>

  <div class="price-badge">$25</div>
  <div class="price-unit">per person</div>

  <div class="dish-illustration" role="img" aria-label="Line illustration of a steaming covered serving dish"></div>

  <nav class="actions">
    <a class="action-button" href="#">ORDER ONLINE</a>
    <a class="action-button" href="#">BOOK A TABLE</a>
    <a class="action-button" href="#">GIFT VOUCHER</a>
  </nav>

  <div class="brand-name">CEDAR FORK<br>GRILLHOUSE</div>
</main>
</body>
</html>
```